Ridgeway Sparks Business cards

We require somebody to design business cards for our new business.

Target Market(s)

Mining, haulage and civil.

Industry/Entity Type

Auto electrician in mining industry

Contact Information for Business Card

ABN, business email address, mobile number.

Colors
00AB8E
00BBA5
67D7C9
C6EFE9
E9F9F6

Requirements
Must have
• Services I offer: Breakdowns, Field Service, A/C Systems, Machine rewires, mine site vehicle fit outs

```html
<!DOCTYPE html>
<html lang="en">
<head>
<meta charset="utf-8">
<title>Ridgeway Sparks Business Cards</title>
<link href="https://fonts.googleapis.com/css2?family=Montserrat:wght@400;500;700;800&display=swap" rel="stylesheet">
<style>
  :root {
    --backdrop: #2b2b2b;
    --card: #161616;
    --teal: #4fc7bb;
    --teal-deep: #00ab8e;
    --white: #f2f2f2;
  }
  * { margin: 0; padding: 0; box-sizing: border-box; }
  html, body { width: 1200px; height: 1108px; overflow: hidden; }
  body {
    background: var(--backdrop);
    font-family: "Montserrat", sans-serif;
    color: var(--white);
    position: relative;
  }
  .card {
    position: absolute;
    top: 180px;
    width: 450px;
    height: 740px;
    background: var(--card);
    border-radius: 24px;
    display: flex;
    flex-direction: column;
    align-items: center;
    text-align: center;
  }
  .card--front { left: 110px; }
  .card--back { left: 640px; }

  .brand-name {
    font-weight: 800;
    color: var(--teal);
    text-transform: uppercase;
    letter-spacing: 1px;
    line-height: 1.05;
  }
  .card--front .brand-name { margin-top: 120px; font-size: 40px; }
  .card--back .brand-name { margin-top: 250px; font-size: 58px; }

  .person-name {
    margin-top: 70px;
    font-size: 30px;
    font-weight: 800;
    color: var(--teal);
    text-transform: uppercase;
  }
  .person-role { margin-top: 4px; font-size: 20px; font-weight: 400; }

  .divider {
    position: relative;
    width: 300px;
    height: 30px;
    margin-top: 22px;
    display: flex;
    justify-content: center;
    align-items: center;
    gap: 8px;
  }
  .divider::before {
    content: "";
    position: absolute;
    left: 0; right: 0; top: 50%;
    border-top: 2px solid var(--teal);
  }
  .icon {
    position: relative;
    width: 30px; height: 30px;
    border-radius: 50%;
    background: var(--teal);
    display: flex; align-items: center; justify-content: center;
  }
  .icon svg { width: 16px; height: 16px; }

  .contact-list { margin-top: 12px; font-size: 18px; line-height: 1.45; }
  .address { margin-top: 12px; font-size: 18px; line-height: 1.45; }
  .abn { margin-top: 26px; font-size: 19px; color: var(--teal); }

  .services-title {
    margin-top: auto;
    font-size: 22px;
    font-weight: 800;
    color: var(--teal);
    text-decoration: underline;
    text-underline-offset: 4px;
  }
  .services-list {
    margin: 8px 0 70px;
    font-size: 21px;
    font-weight: 500;
    line-height: 1.5;
  }
  .bullet { color: var(--teal); }
</style>
</head>
<body>
  <section class="card card--front">
    <div class="brand-name">Ridgeway<br>Sparks</div>
    <div class="person-name">Marcus Delaney</div>
    <div class="person-role">Founder &amp; CEO</div>

    <div class="divider">
      <span class="icon" aria-label="Phone">
        <svg viewBox="0 0 24 24"><path fill="#161616" d="M6.6 10.8a15.1 15.1 0 0 0 6.6 6.6l2.2-2.2c.3-.3.7-.4 1-.2 1.1.4 2.3.6 3.6.6.6 0 1 .4 1 1V20c0 .6-.4 1-1 1C10.6 21 3 13.4 3 4c0-.6.4-1 1-1h3.5c.6 0 1 .4 1 1 0 1.3.2 2.5.6 3.6.1.3 0 .7-.2 1z"/></svg>
      </span>
      <span class="icon" aria-label="Email">
        <svg viewBox="0 0 24 24"><rect x="3" y="6" width="18" height="12" rx="1.5" fill="#161616"/><path d="M3.5 6.5 12 13l8.5-6.5" fill="none" stroke="#4fc7bb" stroke-width="1.6"/></svg>
      </span>
      <span class="icon" aria-label="Website">
        <svg viewBox="0 0 24 24" fill="none" stroke="#161616" stroke-width="2"><circle cx="12" cy="12" r="9"/><path d="M3 12h18M12 3c3 3 3 15 0 18M12 3c-3 3-3 15 0 18"/></svg>
      </span>
    </div>

    <div class="contact-list">
      <div>0755 218 4406</div>
      <div>info@ridgewaysparks.com</div>
      <div>ridgewaysparks.com</div>
    </div>

    <div class="divider">
      <span class="icon" aria-label="Location">
        <svg viewBox="0 0 24 24"><path fill="#161616" d="M12 2a7 7 0 0 0-7 7c0 5 7 13 7 13s7-8 7-13a7 7 0 0 0-7-7zm0 9.5A2.5 2.5 0 1 1 12 6.5a2.5 2.5 0 0 1 0 5z"/></svg>
      </span>
    </div>

    <div class="address">
      <div>1280 W. Copper Ridge Rd #14</div>
      <div>Ashford, Utah 84120</div>
    </div>

    <div class="abn">ABN No - 04718263</div>
  </section>

  <section class="card card--back">
    <div class="brand-name">Ridgeway<br>Sparks</div>
    <div class="services-title">SERVICES:</div>
    <div class="services-list">
      <div><span class="bullet">•</span> Breakdowns <span class="bullet">•</span> Field Service</div>
      <div><span class="bullet">•</span> A/C Systems <span class="bullet">•</span> Machine rewires</div>
      <div><span class="bullet">•</span> Mine site vehicle fit outs</div>
    </div>
  </section>
</body>
</html>
```